I need a movie poster design for a short film.

The poster should have a BLUE handball with a old school headband around the top like a person would wear. I was thinking a blue background but ill leave that open. Can you also put the title Tin Hearts on the poster.

its a racquetball, all blue ball, solid blue no groves, clean looking, sharp poster, thanks

white headband with, blue and red strip.

```html
<!DOCTYPE html>
<html lang="en">
<head>
<meta charset="utf-8">
<title>Tin Hearts — Poster</title>
<link rel="stylesheet" href="https://fonts.googleapis.com/css2?family=Oswald:wght@300&display=swap">
<style>
  :root {
    --navy-deep: #062a63;
    --navy: #0b3f8a;
    --royal: #1a5fae;
    --sky: #4f93d6;
    --glow: #eef5fc;
    --ball-light: #3f86c9;
    --ball-mid: #2467a8;
    --ball-dark: #123f72;
    --title: #ffffff;
  }
  html, body {
    margin: 0;
    padding: 0;
    overflow: hidden;
  }
  .poster {
    position: relative;
    width: 848px;
    height: 1200px;
    overflow: hidden;
    background:
      radial-gradient(ellipse 260px 520px at 560px 40px, var(--glow) 0%, rgba(238,245,252,0.7) 30%, rgba(79,147,214,0) 100%),
      radial-gradient(ellipse 700px 180px at 300px 990px, rgba(210,230,248,0.85) 0%, rgba(79,147,214,0.4) 50%, rgba(79,147,214,0) 100%),
      radial-gradient(ellipse 620px 820px at 500px 480px, var(--sky) 0%, var(--royal) 45%, var(--navy) 75%, var(--navy-deep) 100%);
    background-color: var(--navy);
  }
  .ball-art {
    position: absolute;
    left: 0;
    top: 0;
    width: 848px;
    height: 1200px;
  }
  .title {
    position: absolute;
    right: 61px;
    margin: 0;
    font-family: "Oswald", "Arial Narrow", sans-serif;
    font-weight: 300;
    font-size: 272px;
    line-height: 1;
    color: var(--title);
    text-align: right;
    letter-spacing: 2px;
  }
  .title-line {
    position: absolute;
    right: 0;
    white-space: nowrap;
  }
  .title-line--first { top: 565px; }
  .title-line--second { top: 865px; }
</style>
</head>
<body>
  <main class="poster">
    <svg class="ball-art" viewBox="0 0 848 1200" role="img" aria-label="Solid blue racquetball wearing a white terry headband with a red and a blue stripe">
      <defs>
        <radialGradient id="ballShade" cx="0.45" cy="0.3" r="0.75">
          <stop offset="0" stop-color="var(--ball-light)"/>
          <stop offset="0.55" stop-color="var(--ball-mid)"/>
          <stop offset="1" stop-color="var(--ball-dark)"/>
        </radialGradient>
      </defs>
      <circle cx="262" cy="550" r="405" fill="url(#ballShade)"/>
    </svg>
    <h1 class="title">
      <span class="title-line title-line--first">TIN</span>
      <span class="title-line title-line--second">HEARTS</span>
    </h1>
  </main>
</body>
</html>
```